New graphics package for website

We're currently about to launch a product to insurance agents and we need to upgrade the graphics package for tundlex.io
The current site is http://tundlex.io
We'd like to upgrade the graphics package for this site - very simple. The site needs to have a very modern and elegant feel.
The site content should remain, we may add some. You can use lorem ipsum you need content to fill a space.
We need to add 3 page links - Home, Enroll, Request invitation
We also have an invitation page that needs to be upgraded (shall not be accessible from main site), the current page for that is: http://www.tundlex.io/webinar.php - content on this page cannot change, just needs a graphics over lay.
Final source files shall be AI or PSD and include all fonts and high-res images included.
Target Market(s)
Business to business - insurance agencies across the US are the only users of this site.
Industry/Entity Type
Insurance
Number of Pages Required
2 page
Requirements
Must have
- Multiple forms only in the inner pages:
- Enroll form for the enroll page.
- Invite form for the invite page
- Invite form shall only have name, email, phone, carrier

```html
<!DOCTYPE html>
<html lang="en">
<head>
<meta charset="utf-8">
<title>tundlex.io — Insurance leads for agents</title>
<link href="https://fonts.googleapis.com/css2?family=Open+Sans:wght@400;600;700;800&display=swap" rel="stylesheet">
<style>
:root{
  --orange:#f26522;
  --orange-dark:#d9541a;
  --ink:#333333;
  --muted:#8a8a8a;
  --line:#e4e4e4;
  --band:#3b3b3b;
  --footer:#2a2a2a;
  --paper:#ffffff;
  --soft:#f4f4f4;
}
*{box-sizing:border-box;margin:0;padding:0}
html,body{width:800px;height:1200px;overflow:hidden}
body{font-family:"Open Sans",Arial,sans-serif;color:var(--ink);background:var(--paper);position:relative}
.topbar{height:20px;background:var(--soft);border-bottom:1px solid var(--line);display:flex;align-items:center;justify-content:space-between;padding-left:60px;font-size:8px;color:var(--muted)}
.topbar-cta{background:var(--orange);color:#fff;height:20px;width:118px;display:flex;align-items:center;justify-content:center;font-weight:700;font-size:8px;letter-spacing:.5px;margin-right:40px}
.header{height:79px;display:flex;align-items:center;justify-content:space-between;padding:0 52px 0 60px}
.brand{display:flex;align-items:center;gap:10px}
.brand-dot{width:30px;height:30px;border-radius:50%;background:var(--orange)}
.brand-name{font-size:27px;font-weight:700;color:var(--orange)}
.nav{display:flex;align-items:center;gap:26px;font-size:10px;font-weight:600}
.nav a{color:var(--ink);text-decoration:none;padding-bottom:4px}
.nav a.active{color:var(--orange);border-bottom:2px solid var(--orange)}
.nav-phone{display:flex;align-items:center;gap:6px}
.nav-phone strong{color:var(--orange)}
.hero{position:relative;height:341px;overflow:hidden}
.hero-photo{position:absolute;inset:0;background:linear-gradient(100deg,#7d8590 0%,#aeb4bb 35%,#c9ccd0 60%,#9aa1a8 100%)}
.hero-shade{position:absolute;inset:0;background:linear-gradient(180deg,rgba(0,0,0,0) 40%,rgba(0,0,0,.25) 100%)}
.hero-copy{position:absolute;left:0;right:0;top:150px;text-align:center;color:#fff}
.hero-copy h1{font-size:36px;font-weight:800;text-shadow:0 2px 6px rgba(0,0,0,.35)}
.hero-copy p{font-size:13px;margin-top:6px;color:#ffe2d3;text-shadow:0 1px 4px rgba(0,0,0,.4)}
.hero-dots{position:absolute;top:245px;left:0;right:0;display:flex;justify-content:center;gap:6px}
.hero-dots span{width:7px;height:7px;border-radius:50%;background:rgba(255,255,255,.6)}
.hero-dots span.on{background:var(--orange)}
.services{height:227px;text-align:center;padding-top:24px}
.section-title{color:var(--orange);font-size:13px;font-weight:700;letter-spacing:.5px}
.section-sub{font-size:8px;color:var(--muted);margin-top:4px}
.service-row{display:flex;justify-content:space-between;padding:0 60px;margin-top:30px;text-align:left}
.service{width:160px;display:flex;gap:8px}
.service-icon{flex:0 0 18px}
.service h3{font-size:10px;color:var(--orange);font-weight:600;margin-bottom:5px}
.service p{font-size:8px;line-height:1.5;color:var(--muted)}
.markets{height:226px;background:var(--band);position:relative;color:#d4d4d4;padding:32px 0 0 60px}
.markets h2{font-size:13px;color:#fff;font-weight:700;letter-spacing:.3px}
.markets p{font-size:8.5px;line-height:1.6;width:400px;margin-top:12px}
.btn-outline{display:inline-block;margin-top:16px;border:1px solid #fff;color:#fff;font-size:8px;font-weight:700;padding:6px 14px}
.enroll-card{position:absolute;right:52px;top:20px;width:180px;height:190px;background:#fff;border-bottom:3px solid var(--orange)}
.enroll-card h4{background:var(--orange);color:#fff;font-size:8px;font-weight:700;text-align:center;height:26px;line-height:26px}
.enroll-form{padding:10px 12px}
.field{height:18px;border:1px solid var(--line);font-size:7px;color:var(--muted);padding:0 6px;line-height:16px;margin-bottom:8px}
.btn-solid{background:var(--orange);color:#fff;font-size:8px;font-weight:700;text-align:center;height:22px;line-height:22px;margin-top:4px}
.lower{display:flex;justify-content:space-between;padding:28px 52px 0 60px;height:227px}
.blog{width:300px}
.col-head{display:flex;justify-content:space-between;align-items:center;border-bottom:1px solid var(--line);padding-bottom:6px;font-size:12px;font-weight:700}
.col-head span{color:var(--orange)}
.arrows{display:flex;gap:4px}
.arrows i{width:14px;height:14px;border:1px solid var(--line);display:block}
.blog-row{display:flex;gap:12px;margin-top:14px}
.post{width:144px}
.post-photo{height:92px;border:1px solid var(--line)}
.post-photo.a{background:linear-gradient(135deg,#c8b39c,#8fb0c8)}
.post-photo.b{background:linear-gradient(135deg,#4a5a78,#1f2838)}
.post p{font-size:8px;color:var(--orange);margin-top:6px}
.news{width:330px}
.news-item{display:flex;gap:10px;margin-top:12px}
.news-date{flex:0 0 30px;height:30px;background:var(--orange);color:#fff;font-size:7px;font-weight:700;text-align:center;line-height:1.2;padding-top:6px}
.news-item h5{font-size:8px;color:var(--orange);font-weight:700}
.news-item p{font-size:7.5px;color:var(--muted);line-height:1.5;margin-top:2px}
.footer{position:absolute;left:0;right:0;bottom:0;height:80px;background:var(--footer);display:flex;align-items:center;justify-content:space-between;padding:0 52px 0 60px;color:#999;font-size:7.5px}
.footer-brand{display:flex;align-items:center;gap:12px}
.footer-brand .brand-dot{width:22px;height:22px}
.footer-brand .brand-name{font-size:18px}
.footer-meta p{line-height:1.7}
.social{display:flex;align-items:center;gap:8px}
.social i{width:18px;height:18px;border-radius:50%;background:#555;display:block}
</style>
</head>
<body>
<div class="topbar"><span>Welcome to our insurance agent network</span><span class="topbar-cta">ENROLL NOW</span></div>
<header class="header">
  <div class="brand"><span class="brand-dot"></span><span class="brand-name">tundlex.io</span></div>
  <nav class="nav">
    <a class="active">Home</a><a>Enroll</a><a>Request Invitation</a><a>Contact us</a>
    <span class="nav-phone"><svg width="10" height="10" viewBox="0 0 24 24"><path fill="#f26522" d="M6.6 10.8a15 15 0 0 0 6.6 6.6l2.2-2.2c.3-.3.7-.4 1-.2 1.1.4 2.3.6 3.6.6.6 0 1 .4 1 1V20c0 .6-.4 1-1 1A17 17 0 0 1 3 4c0-.6.4-1 1-1h3.5c.6 0 1 .4 1 1 0 1.3.2 2.5.6 3.6.1.3 0 .7-.2 1z"/></svg>Call Us: <strong>(888) 555-0147</strong></span>
  </nav>
</header>
<section class="hero">
  <div class="hero-photo" role="img" aria-label="Photo of a team of business people in an office"></div>
  <div class="hero-shade"></div>
  <div class="hero-copy">
    <h1>Making insurance leads obsolete</h1>
    <p>Sed do eiusmod tempor incididunt ut labore et dolore magna aliqua.</p>
  </div>
  <div class="hero-dots"><span></span><span class="on"></span><span></span></div>
</section>
<section class="services">
  <div class="section-title">WHAT WE DO?</div>
  <div class="section-sub">Simply dummy text of the printing and typesetting industry. Lorem Ipsum.</div>
  <div class="service-row">
    <div class="service"><svg class="service-icon" viewBox="0 0 18 18"><circle cx="9" cy="9" r="8" fill="#f26522"/><path d="M5 9l3 3 5-6" stroke="#fff" stroke-width="2" fill="none"/></svg><div><h3>Enhance leadership</h3><p>Sit voluptatem accusantium doloremque laudantium, totam rem aperiam eaque.</p></div></div>
    <div class="service"><svg class="service-icon" viewBox="0 0 18 18"><rect x="2" y="3" width="14" height="12" rx="2" fill="#f26522"/><path d="M5 7h8M5 10h6" stroke="#fff" stroke-width="1.5"/></svg><div><h3>Aperiam eaque ipsa</h3><p>Sit voluptatem accusantium doloremque laudantium, totam rem aperiam eaque.</p></div></div>
    <div class="service"><svg class="service-icon" viewBox="0 0 18 18"><circle cx="9" cy="9" r="5" fill="none" stroke="#f26522" stroke-width="3"/><circle cx="9" cy="9" r="1.8" fill="#f26522"/></svg><div><h3>Dolorem ipsum quia</h3><p>Sit voluptatem accusantium doloremque laudantium, totam rem aperiam eaque.</p></div></div>
    <div class="service"><svg class="service-icon" viewBox="0 0 18 18"><circle cx="9" cy="6" r="3.5" fill="#f26522"/><path d="M2 17c0-4 3-6 7-6s7 2 7 6z" fill="#f26522"/></svg><div><h3>Our Benefits protection</h3><p>Sit voluptatem accusantium doloremque laudantium, totam rem aperiam eaque.</p></div></div>
  </div>
</section>
<section class="markets">
  <h2>DOMINATE YOUR LOCAL INSURANCE MARKETS</h2>
  <p>A new type of insurance marketing product that takes the leads used by internet lead aggregators and offers them to insurance agents for a low monthly fee. Opt out the middle man by dispatching endpoints set in the web and leverage mobile device searching to get you great quality prospects.</p>
  <p>We leverage everything for you. We only sell one product, and it's awesome.</p>
  <span class="btn-outline">READ MORE</span>
  <div class="enroll-card">
    <h4>ENROLL FOR FREE INVITATION</h4>
    <div class="enroll-form">
      <div class="field">Name</div><div class="field">Email</div><div class="field">Phone</div><div class="field">Carrier</div>
      <div class="btn-solid">ENROLL</div>
    </div>
  </div>
</section>
<section class="lower">
  <div class="blog">
    <div class="col-head"><div><span>RECENTLY</span> BLOG</div><div class="arrows"><i></i><i></i></div></div>
    <div class="blog-row">
      <div class="post"><div class="post-photo a" role="img" aria-label="Photo of a smiling family outdoors"></div><p>Lorem ipsum dolor sit</p></div>
      <div class="post"><div class="post-photo b" role="img" aria-label="Photo of business people holding umbrellas"></div><p>Lorem ipsum dolor sit</p></div>
    </div>
  </div>
  <div class="news">
    <div class="col-head"><div><span>LATEST</span> NEWS</div></div>
    <div class="news-item"><div class="news-date">15<br>JUN</div><div><h5>NEWS HEADLINE HERE</h5><p>Lorem ipsum dolor sit amet, consectetur adipiscing elit, sed do eiusmod tempor.</p></div></div>
    <div class="news-item"><div class="news-date">12<br>JUN</div><div><h5>NEWS HEADLINE HERE</h5><p>Lorem ipsum dolor sit amet, consectetur adipiscing elit, sed do eiusmod tempor.</p></div></div>
    <div class="news-item"><div class="news-date">08<br>JUN</div><div><h5>NEWS HEADLINE HERE</h5><p>Lorem ipsum dolor sit amet, consectetur adipiscing elit, sed do eiusmod tempor.</p></div></div>
  </div>
</section>
<footer class="footer">
  <div class="footer-brand">
    <span class="brand-dot"></span><span class="brand-name">tundlex.io</span>
    <div class="footer-meta"><p>Home | Enroll | Request Invitation | Contact us</p><p>© 2024 tundlex.io. All rights reserved.</p></div>
  </div>
  <div class="social"><span>Connect with us on social media</span><i></i><i></i><i></i><i></i></div>
</footer>
</body>
</html>
```